Restaurant Facility Equipment & Store Maintenance/

I need a flyer showing commercial/industrial kitchen equipment photos we work on Hot Equipment & Cold Equipment and offer many services. see attached highlights

```html
<!DOCTYPE html>
<html lang="en">
<head>
<meta charset="utf-8">
<title>Kitchen Keeper – Restaurant Equipment &amp; Facility Maintenance Flyer</title>
<link href="https://fonts.googleapis.com/css2?family=Open+Sans:wght@400;600;700;800&family=Yellowtail&display=swap" rel="stylesheet">
<style>
  :root {
    --stage: #d3d8d4;
    --blue: #1374c9;
    --navy: #2b2a7a;
    --gold: #e4a81c;
    --gold-light: #f6d04a;
    --red: #d8202f;
    --white: #ffffff;
    --ink: #111111;
  }
  * { box-sizing: border-box; margin: 0; padding: 0; }
  html, body { width: 1200px; height: 800px; overflow: hidden; }
  body {
    background: var(--stage);
    font-family: "Open Sans", Arial, sans-serif;
    position: relative;
  }
  .flyer {
    position: absolute;
    left: 330px; top: 18px;
    width: 540px; height: 764px;
    background: var(--blue);
    overflow: hidden;
    box-shadow: 3px 4px 8px rgba(0,0,0,.25);
  }
  .hero-photo {
    position: absolute; left: 0; top: 0; width: 540px; height: 352px;
    background:
      linear-gradient(180deg, var(--blue) 0%, var(--blue) 24%, rgba(19,116,201,.55) 34%, rgba(19,116,201,0) 46%),
      linear-gradient(180deg, #b9c2cc 40%, #8f969d 70%, #5f656b 100%);
  }
  .headline {
    position: absolute; left: 0; top: 10px; width: 540px;
    text-align: center; color: var(--white);
    font-weight: 800; font-size: 22.5px; line-height: 23.5px;
  }
  .promise-arrow { position: absolute; left: 0; top: 0; }
  .promise-text {
    position: absolute; left: 346px; top: 262px; width: 190px;
    color: var(--white); font-weight: 800; font-size: 16.5px; line-height: 19px;
    transform: rotate(7deg); transform-origin: left top;
  }
  .gold-rule {
    position: absolute; left: 0; top: 352px; width: 540px; height: 11px;
    background: linear-gradient(90deg, #b57f12, var(--gold-light) 45%, #c58f16 75%, var(--gold-light));
  }
  .services-title {
    position: absolute; left: 0; top: 374px; width: 540px;
    text-align: center; color: var(--navy); white-space: nowrap;
    font-weight: 800; font-size: 17.5px; line-height: 20.5px;
  }
  .service-list {
    position: absolute; top: 446px; list-style: none;
    color: var(--white); font-size: 10.3px; line-height: 10.5px;
  }
  .service-list.left { left: 19px; width: 262px; }
  .service-list.right { left: 283px; width: 252px; }
  .service-list li { position: relative; padding-left: 14px; margin-bottom: 5.6px; }
  .service-list li::before {
    content: ""; position: absolute; left: 0; top: 2px;
    width: 6px; height: 6px; border-radius: 50%; background: var(--gold);
  }
  .footer { position: absolute; left: 0; top: 620px; width: 540px; height: 144px; }
  .footer-shapes { position: absolute; left: 0; top: 0; }
  .call-to-action {
    position: absolute; left: 16px; top: 12px; width: 232px;
    font-weight: 700; font-size: 11.2px; line-height: 14.4px; color: var(--ink);
  }
  .badge { position: absolute; top: 99px; height: 22px; border-radius: 5px; }
  .badge.cert { left: 26px; width: 69px; border: 3px solid var(--red); background: var(--white); }
  .badge.safety { left: 126px; width: 68px; background: var(--navy); }
  .tagline {
    position: absolute; right: 34px; top: 2px; white-space: nowrap;
    font-family: "Yellowtail", cursive; color: var(--red);
    font-size: 18px; line-height: 20px; transform: rotate(-6deg); transform-origin: right center;
  }
  .brand-name {
    position: absolute; right: 16px; top: 34px; text-align: right;
    font-weight: 800; font-size: 32px; line-height: 34px; color: var(--ink);
  }
  .phone {
    position: absolute; right: 12px; top: 104px;
    font-weight: 800; font-size: 21px; line-height: 28px; color: var(--red);
  }
</style>
</head>
<body>
  <main class="flyer">
    <div class="hero-photo" role="img" aria-label="Photo of a stainless steel commercial kitchen with stock pots, ranges, ovens and colourful wall tiles"></div>
    <h1 class="headline">Installation, Rebuilds, Safety Inspection, and<br>Preventive Maintenance Services for<br>Denver Metro and Surrounding Areas</h1>

    <svg class="promise-arrow" width="540" height="352" viewBox="0 0 540 352" aria-hidden="true">
      <defs>
        <linearGradient id="arrowFill" x1="0" x2="1">
          <stop offset="0" stop-color="#d8202f"/>
          <stop offset=".7" stop-color="#c81a29"/>
          <stop offset="1" stop-color="#8e121d"/>
        </linearGradient>
      </defs>
      <polygon points="498,232 540,250 540,300 520,300" fill="#9d1420"/>
      <polygon points="306,262 352,214 355,242 510,262 540,268 540,348 500,346 346,322 343,350" fill="url(#arrowFill)"/>
    </svg>
    <p class="promise-text">We handle<br>everything from<br>the front door<br>to the back door</p>

    <div class="gold-rule"></div>

    <h2 class="services-title">We offer hot and cold equipment<br>repair, cleaning, maintenance, handyman work, drywall,<br>painting, door closers, floors, and ceiling tiles.</h2>

    <ul class="service-list left">
      <li>KSTA Certified Technicians</li>
      <li>Round-the-clock emergency services</li>
      <li>Customers who subscribe to preventive maintenance services receive a reduced rate on hourly labor charges</li>
      <li>Original equipment manufacturer (OEM) parts</li>
      <li>30-day warranty on all OEM parts installed</li>
      <li>Equipment Cleaning &amp; Rebuilds</li>
      <li>Used equipment available for purchase or rental</li>
      <li>Specialized Programs for Preventive<br>Maintenance of Equipment</li>
    </ul>
    <ul class="service-list right">
      <li>Installation and Repair of Restaurant Equipment</li>
      <li>Repair or replace restaurant furniture</li>
      <li>Comprehensive licensed electrical contractor services for both interior and exterior projects, including lighting system upgrades.</li>
      <li>Building Graffiti Removal Services</li>
      <li>Hot &amp; Cold Equipment</li>
      <li>Food Service Trucks</li>
      <li>We repair floors, walls, counters, décor, signage, parking lots, dumpsters, and more.</li>
    </ul>

    <footer class="footer">
      <svg class="footer-shapes" width="540" height="144" viewBox="0 0 540 144" aria-hidden="true">
        <defs>
          <linearGradient id="goldSweep" x1="0" x2="1">
            <stop offset="0" stop-color="#c58f16"/>
            <stop offset=".55" stop-color="#e4a81c"/>
            <stop offset="1" stop-color="#f6e04a"/>
          </linearGradient>
        </defs>
        <rect width="540" height="144" fill="#d9d9dc"/>
        <path d="M0 0 H262 C250 40 232 70 200 84 H0 Z" fill="url(#goldSweep)"/>
        <path d="M0 84 H200 C232 90 248 115 252 144 H0 Z" fill="#ffffff"/>
      </svg>
      <p class="call-to-action">For any need in your restaurant, call us and we will send a skilled technician to manage all your commercial and industrial facility requirements.</p>
      <div class="badge cert" role="img" aria-label="Certified technician badge"></div>
      <div class="badge safety" role="img" aria-label="Safety compliance badge"></div>
      <p class="tagline">If you have it, we probably fix it</p>
      <p class="brand-name">Kitchen<br>Keeper</p>
      <p class="phone">(000) 555-0142</p>
    </footer>
  </main>
</body>
</html>
```